Label Redesign For Hemp Oil Tincture Bottle*

I need a label redesigned for Marbleleaf Hemp, current bottle label and logo is attached. The current label doesn't standout, not sure if its the font size or colors on the existing label. It is very important to have on the label that this is a Premium Full Spectrum Hemp Oil that is 2000mg. Then after the label is redesigned and approved, I would need to packaging to be designed to match the approved label design.
This Hemp oil has a relaxing effect to help ease mental and emotional stress, tension and worry. The Omega Fatty Acids it contains also naturally improves your mood and overall brain function, causing you to feel more alert and focused. Hemp Oil helps with insomnia. Take some 2-3 hours before bedtime, you will feel relaxed yet aware of how tired you are that it will lead to a good night's sleep. Hemp Oil helps ease chronic pain and inflammation from conditions such as arthritis, fibromyalgia, lupus, and MS. As a pain relief supplement, it is a safer, natural, non-chemical and non-addictive alternative to prescription painkillers.

Target Market(s)

Adults

Industry/Entity Type

Supplement

Font styles to use
Serif
Sans Serif

Colors

Designer to choose colors to be used in the design.

Requirements
Must have
• All information thats on current label but where it says 750 in the front of the existing label, it needs to say 2000. The 2000 should be prominent on the label.

```html
<!DOCTYPE html>
<html lang="en">
<head>
<meta charset="utf-8">
<title>Marbleleaf Hemp – Hemp Oil Label</title>
<link href="https://fonts.googleapis.com/css2?family=Cinzel:wght@400&family=Tinos:wght@400;700&display=swap" rel="stylesheet">
<style>
  :root{
    --page:#eef0ed;
    --teal-dark:#2f4c52;
    --teal-frame:#3d5f63;
    --cream:#ecefd6;
    --cream-soft:#f3f4e4;
    --ink:#3b4a4c;
    --label-top:#e6e9ee;
    --label-mid:#dfe3dc;
    --label-bot:#e9dfe3;
    --leaf-green:#b9cf9c;
  }
  *{box-sizing:border-box;margin:0;padding:0}
  html,body{width:1200px;height:1200px;overflow:hidden}
  body{background:var(--page);font-family:"Tinos",serif;color:var(--ink);position:relative}

  .brand-band{position:absolute;left:0;top:150px;width:1200px;height:100px;background:var(--cream);display:flex;align-items:center;justify-content:center;gap:36px}
  .brand-band__name{font-family:"Cinzel",serif;font-size:64px;letter-spacing:2px;color:var(--teal-dark)}
  .brand-band__dot{width:70px;height:70px;border-radius:50%;background:var(--leaf-green)}

  .label{position:absolute;left:60px;top:330px;width:1080px;height:760px;display:grid;grid-template-columns:1fr 1fr 1fr;border:1px solid #cfd3cf}
  .label__pattern{position:absolute;inset:0;background:linear-gradient(180deg,var(--label-top),var(--label-mid) 55%,var(--label-bot))}
  .panel{position:relative;padding:40px 34px;display:flex;flex-direction:column;gap:34px}

  .info-box{background:var(--cream-soft);border:3px double var(--teal-frame);padding:18px 20px;font-size:17px;line-height:1.35;text-align:justify}
  .info-box__title{font-size:16px;text-transform:uppercase;letter-spacing:1px;text-align:center;margin-bottom:10px}
  .info-box--center{text-align:center;text-transform:uppercase;font-size:15px;letter-spacing:.5px}

  .front{padding:34px 24px}
  .front__frame{height:100%;border:2px solid var(--teal-frame);padding:14px;display:flex;flex-direction:column}
  .front__logo-area{background:var(--teal-dark);height:130px;display:flex;align-items:center;justify-content:center;gap:14px}
  .front__logo-dot{width:36px;height:36px;border-radius:50%;background:var(--leaf-green)}
  .front__logo-name{font-family:"Tinos",serif;font-size:26px;color:var(--cream)}
  .front__brand-strip{background:var(--cream);text-align:center;font-size:17px;letter-spacing:1px;padding:6px 0;text-transform:uppercase}
  .front__main{background:var(--teal-dark);color:var(--cream);text-align:center;padding:14px 0 26px}
  .front__pill{display:inline-block;background:var(--cream);color:var(--teal-dark);border-radius:14px;padding:2px 26px;font-size:20px;margin-bottom:16px}
  .front__spectrum{font-size:24px;font-weight:700}
  .front__number{font-size:24px;font-weight:700;margin:6px 0}
  .front__product{font-size:36px;font-weight:700;letter-spacing:1px}
  .front__dose{background:var(--cream);text-align:center;padding:16px 0;flex:1;display:flex;flex-direction:column;justify-content:center;gap:8px}
  .front__mg{font-size:40px}
  .front__type{font-size:18px;letter-spacing:1px}
  .front__vol{font-size:16px}
  .front__flavour{background:var(--teal-dark);color:var(--cream);text-align:center;font-size:22px;padding:8px 0;margin-top:14px}

  .facts{font-size:13px;text-align:left}
  .facts__row{display:flex;justify-content:space-between;border-bottom:1px solid #b8c0bd;padding:3px 0}
  .facts__note{margin-top:10px}
</style>
</head>
<body>
  <header class="brand-band">
    <span class="brand-band__name">MARBLELEAF HEMP</span>
    <span class="brand-band__dot"></span>
  </header>

  <section class="label">
    <div class="label__pattern" role="img" aria-label="Soft pastel hemp leaf pattern over pale horizontal stripes"></div>

    <div class="panel panel--left">
      <div class="info-box">
        <p class="info-box__title">Suggested Use</p>
        <p>Shake well before each use. Take 30 drops (1 full dropper) and place it in mouth for 90 seconds 1–2 times daily or as recommended by physician.</p>
      </div>
      <div class="info-box">
        <p class="info-box__title">Warning:</p>
        <p>If you are pregnant or breast feeding, consult a health care professional before use.</p>
      </div>
      <div class="info-box info-box--center">
        <p>Keep out of reach of children</p>
        <p style="margin-top:12px">Do not use if seal is broken or missing</p>
      </div>
    </div>

    <div class="panel front">
      <div class="front__frame">
        <div class="front__logo-area">
          <span class="front__logo-dot"></span>
          <span class="front__logo-name">Marbleleaf Hemp</span>
        </div>
        <div class="front__brand-strip">Marbleleaf Hemp</div>
        <div class="front__main">
          <span class="front__pill">Zero THC</span>
          <p class="front__spectrum">Premium Full Spectrum</p>
          <p class="front__number">2000</p>
          <p class="front__product">HEMP OIL</p>
        </div>
        <div class="front__dose">
          <p class="front__mg">2000 mg</p>
          <p class="front__type">DIETARY SUPPLEMENT</p>
          <p class="front__vol">1floz (30ml)</p>
        </div>
        <div class="front__flavour">Natural Peppermint flavour</div>
      </div>
    </div>

    <div class="panel panel--right">
      <div class="info-box facts">
        <p class="info-box__title">Supplement Facts</p>
        <div class="facts__row"><span>Serving size: 1ml</span></div>
        <div class="facts__row"><span>Servings per Container: 30</span></div>
        <div class="facts__row"><span>Calories</span><span>8 Calories from fat 8</span></div>
        <div class="facts__row"><span>Total fat</span><span>1g 2%</span></div>
        <div class="facts__row"><span>Full Spectrum Hemp Extract</span><span>66.6mg</span></div>
        <p class="facts__note">Other Ingredients: Hemp seed oil, Grapeseed oil, Peppermint &amp; Stevia.</p>
      </div>
    </div>
  </section>
</body>
</html>
```